Certificate of Completion - Educational Trainings

We are looking for a certificate of completion for individuals who complete one of our specific trainings. Files should be provided in a Word (docx) or PowerPoint (pptx) format. The "Talmoray example.png" file is to show necessary information. Copies of logos have been included for design purposes.

Target Market(s)

Training Participants

Industry/Entity Type

Healthcare

Font styles to use
Sans Serif

```html
<!DOCTYPE html>
<html lang="en">
<head>
<meta charset="UTF-8">
<title>Talmoray Certificate of Completion</title>
<link href="https://fonts.googleapis.com/css2?family=Montserrat:wght@300;400;800&display=swap" rel="stylesheet">
<style>
  :root {
    --forest: #106a2e;
    --leaf: #6aad50;
    --ink: #111111;
    --paper: #ffffff;
  }
  * { margin: 0; padding: 0; box-sizing: border-box; }
  html, body { width: 1200px; height: 900px; overflow: hidden; background: var(--paper); }
  body { font-family: 'Montserrat', sans-serif; color: var(--ink); }
  .certificate { position: relative; width: 1200px; height: 900px; background: var(--paper); }
  .frame { position: absolute; inset: 0; width: 1200px; height: 900px; }
  .ornament {
    position: absolute;
    background: radial-gradient(circle, rgba(106,173,80,0.35), rgba(106,173,80,0.05) 70%);
    border-radius: 40%;
  }
  .ornament--top-right { left: 1058px; top: 30px; width: 106px; height: 95px; }
  .ornament--bottom-left { left: 33px; top: 770px; width: 105px; height: 101px; }
  .centered { position: absolute; left: 0; width: 1200px; text-align: center; white-space: nowrap; }
  .brand-mark { top: 64px; display: flex; justify-content: center; }
  .brand-mark span { width: 78px; height: 78px; border-radius: 50%; background: var(--forest); }
  .brand-name { top: 180px; font-weight: 800; font-size: 50px; letter-spacing: 5px; line-height: 1; }
  .issuer-details { top: 241px; font-weight: 400; font-size: 18px; line-height: 25px; letter-spacing: 0.4px; }
  .stars { top: 318px; color: var(--forest); font-size: 17px; letter-spacing: 3px; }
  .title { top: 372px; font-weight: 300; font-size: 45px; letter-spacing: 3.6px; line-height: 1; }
  .awarded-to { top: 458px; font-weight: 300; font-size: 24px; letter-spacing: 1px; line-height: 1; }
  .recipient-line { position: absolute; left: 176px; top: 539px; width: 848px; height: 2px; background: var(--ink); }
  .course { top: 557px; font-weight: 300; font-size: 22.5px; letter-spacing: 0.5px; line-height: 30px; }
  .course-meta { top: 593px; font-weight: 300; font-size: 22.5px; letter-spacing: 0.5px; line-height: 30px; }
  .course-meta .divider { color: var(--leaf); margin: 0 22px; }
  .credits { top: 630px; font-weight: 300; font-size: 27px; color: var(--forest); letter-spacing: 1px; line-height: 34px; }
  .seal { top: 696px; display: flex; justify-content: center; align-items: center; gap: 10px; }
  .seal-name { font-weight: 800; font-size: 22px; letter-spacing: 2px; color: var(--forest); }
  .seal-dot { width: 16px; height: 16px; border-radius: 50%; background: var(--leaf); }
  .signature { position: absolute; top: 752px; border-top: 1.5px solid var(--ink); text-align: center; padding-top: 5px; font-weight: 300; font-size: 21px; line-height: 26px; letter-spacing: 0.6px; white-space: nowrap; }
  .signature--date { left: 186px; width: 256px; }
  .signature--consultant { left: 751px; width: 272px; }
  .accreditation-note { top: 806px; font-weight: 400; font-size: 12.2px; line-height: 16px; letter-spacing: 0.4px; }
</style>
</head>
<body>
<main class="certificate">
  <svg class="frame" viewBox="0 0 1200 900" aria-hidden="true">
    <g fill="var(--forest)">
      <rect x="22" y="15" width="293" height="29"/>
      <rect x="22" y="15" width="29" height="293"/>
      <rect x="1148" y="591" width="29" height="293"/>
      <rect x="884" y="855" width="293" height="29"/>
    </g>
    <g fill="none" stroke="var(--leaf)" stroke-width="0.8">
      <polyline points="375,55 63,55 63,247"/>
      <polyline points="1131,648 1131,841 818,841"/>
      <line x1="315" y1="29" x2="1058" y2="29"/>
      <line x1="1162" y1="125" x2="1162" y2="591"/>
      <line x1="34" y1="308" x2="34" y2="770"/>
      <line x1="138" y1="870" x2="884" y2="870"/>
    </g>
    <g fill="none" stroke="var(--leaf)" stroke-width="3" stroke-linecap="round">
      <polyline points="232,72 79,72 79,328"/>
      <polyline points="1115,569 1115,825 963,825"/>
    </g>
  </svg>

  <div class="ornament ornament--top-right" role="img" aria-label="Decorative vine with small leaves"></div>
  <div class="ornament ornament--bottom-left" role="img" aria-label="Decorative vine with small leaves"></div>

  <div class="centered brand-mark"><span></span></div>
  <h1 class="centered brand-name">TALMORAY</h1>
  <p class="centered issuer-details">48 Harbor Lane, STE. 310 Cedarport, ME 04990<br>Learning Registry Sponsor Number 70583</p>

  <div class="centered stars">★★★</div>
  <h2 class="centered title">CERTIFICATE OF COMPLETION</h2>
  <p class="centered awarded-to">THIS CERTIFICATE IS AWARDED TO</p>
  <div class="recipient-line"></div>

  <p class="centered course">For successful completion of Best Practices: Budget Process / Budget Building</p>
  <p class="centered course-meta">Completed Online<span class="divider">|</span>Field of Study Finance</p>
  <p class="centered credits">CPE Credits: 1</p>

  <div class="centered seal"><span class="seal-dot"></span><span class="seal-name">TALMORAY</span></div>

  <div class="signature signature--date">COMPLETION DATE</div>
  <div class="signature signature--consultant">SENIOR CONSULTANT</div>

  <p class="centered accreditation-note">In accordance with the standard of the Learning Registry of CPE Sponsors. CPE<br>Credits have been granted based on a a 50 minute hour.</p>
</main>
</body>
</html>
```